Wills & Estates legal firm needing A4 presentation folder design

We need a more corporate but family orientated looking presentation folder incorporating existing logo. Needs to be clean lines but warm not clinical. Will contain all documents a family needs when someone dies. Not looking for traditional legal symbols of scales etc. Potential that the design can flow through to letterhead, document front covers, brochures, business cards etc for a complete corporate identity. We are only a firm of one fee earner and cater to a mum and dad market

Industry/Entity Type

Law Firm

Font styles to use
Other font styles liked:
• Univers LT std 57 cn

Colors
ec1f27
848484

Requirements
Must have
• Existing logo
• Area for contact details on back of folder
• Incorporating existing red an grey colours
Should not have
• legal symbols

```html
<!DOCTYPE html>
<html lang="en">
<head>
<meta charset="utf-8">
<title>Hartwell Legal – Presentation Folder</title>
<link rel="stylesheet" href="https://fonts.googleapis.com/css2?family=Roboto+Condensed:wght@400&display=swap">
<style>
  :root {
    --brand-red: #c41230;
    --brand-red-deep: #a50f28;
    --paper: #ffffff;
    --ink: #111111;
    --shadow: rgba(0, 0, 0, 0.28);
  }
  html, body {
    margin: 0;
    padding: 0;
    width: 1200px;
    height: 778px;
    overflow: hidden;
    background: var(--paper);
  }
  .folder-front {
    position: relative;
    width: 1200px;
    height: 778px;
    background: var(--paper);
    overflow: hidden;
    font-family: "Roboto Condensed", "Arial Narrow", sans-serif;
  }
  .brand-name {
    position: absolute;
    left: 62px;
    top: 352px;
    margin: 0;
    font-size: 74px;
    font-weight: 400;
    line-height: 1;
    color: var(--brand-red);
    letter-spacing: 0.5px;
  }
  .corner-art {
    position: absolute;
    inset: 0;
  }
  .card-label {
    font-family: "Roboto Condensed", "Arial Narrow", sans-serif;
    font-size: 29px;
    fill: var(--ink);
  }
  .tagline {
    font-family: "Roboto Condensed", "Arial Narrow", sans-serif;
    font-size: 27px;
    fill: var(--paper);
  }
</style>
</head>
<body>
<main class="folder-front">
  <h1 class="brand-name">Hartwell Legal</h1>

  <svg class="corner-art" width="1200" height="778" viewBox="0 0 1200 778" xmlns="http://www.w3.org/2000/svg">
    <defs>
      <filter id="disc-shadow" x="-10%" y="-10%" width="120%" height="120%">
        <feGaussianBlur in="SourceAlpha" stdDeviation="2"/>
        <feOffset dx="0" dy="0"/>
        <feComponentTransfer><feFuncA type="linear" slope="0.5"/></feComponentTransfer>
        <feMerge><feMergeNode/><feMergeNode in="SourceGraphic"/></feMerge>
      </filter>
      <clipPath id="disc-clip">
        <circle cx="1024" cy="800" r="404"/>
      </clipPath>
      <linearGradient id="inner-arc" x1="0" y1="0" x2="1" y2="1">
        <stop offset="0" stop-color="var(--brand-red-deep)"/>
        <stop offset="0.6" stop-color="var(--brand-red)"/>
      </linearGradient>
      <filter id="label-shadow" x="-10%" y="-10%" width="120%" height="130%">
        <feDropShadow dx="0" dy="1" stdDeviation="1" flood-color="#000" flood-opacity="0.35"/>
      </filter>
    </defs>

    <g class="red-disc">
      <circle cx="1024" cy="800" r="404" fill="var(--brand-red)" filter="url(#disc-shadow)"/>
      <circle cx="1040" cy="920" r="430" fill="url(#inner-arc)" clip-path="url(#disc-clip)"/>
    </g>

    <g class="label-tab" filter="url(#label-shadow)">
      <polygon points="860,494 1062,494 1062,597 1031,628 824,628 824,530" fill="var(--paper)"/>
    </g>
    <text class="card-label" x="942" y="575" text-anchor="middle">Calling Card</text>

    <text class="tagline" x="925" y="690" text-anchor="middle">"Neque porro quisquam est qui</text>
    <text class="tagline" x="925" y="723" text-anchor="middle">dolorem ipsum quia dolor sit amet”</text>
  </svg>
</main>
</body>
</html>
```